Business Cards, stationary for real estate company
Marcie Tolvert Group
Professional
Marcie Tolvert
Real Estate Luxury Specialist
417 Paseo Vista Linda Suite 310 Solana Crest, Ca 90417
marcie@marcietolvertgroup.com
www.marcietolvert.com
DoPLS #04729156
our logo

```html
<!DOCTYPE html>
<html lang="en">
<head>
<meta charset="utf-8">
<title>Marcie Tolvert Group – Business Cards</title>
<link href="https://fonts.googleapis.com/css2?family=Cormorant+Garamond:wght@600&family=Lato:wght@400&display=swap" rel="stylesheet">
<style>
  :root {
    --stage: #8a8a8a;
    --ink: #0d0d0d;
    --paper: #fbfbfb;
    --white: #ffffff;
    --rule: #9a9a9a;
    --text-soft: #3a3a3a;
  }
  * { box-sizing: border-box; margin: 0; padding: 0; }
  html, body { width: 1200px; height: 908px; overflow: hidden; }
  body {
    background: var(--stage);
    display: flex;
    flex-direction: column;
    align-items: center;
    justify-content: center;
    gap: 40px;
    font-family: "Cormorant Garamond", serif;
  }
  .card {
    width: 700px;
    height: 400px;
    border-radius: 22px;
    position: relative;
    overflow: hidden;
  }
  .card--front {
    background: var(--ink);
    color: var(--white);
    display: flex;
    align-items: center;
    justify-content: center;
  }
  .brand {
    display: flex;
    align-items: center;
    gap: 12px;
    white-space: nowrap;
  }
  .brand__mark {
    width: 14px; height: 14px;
    background: currentColor;
    flex: none;
  }
  .brand__name {
    font-weight: 600;
    font-size: 32px;
    line-height: 1;
  }
  .card--back {
    background: var(--paper);
    color: var(--ink);
  }
  .back__logo {
    position: absolute;
    left: 20px; top: 70px;
    width: 330px; height: 230px;
    display: flex; align-items: center; justify-content: center;
  }
  .back__logo .brand__name { font-size: 24px; }
  .back__logo .brand__mark { width: 11px; height: 11px; }
  .back__divider {
    position: absolute;
    left: 365px; top: 60px;
    width: 1px; height: 250px;
    background: var(--rule);
  }
  .contact {
    position: absolute;
    left: 395px; top: 58px;
    right: 20px;
  }
  .contact__name {
    font-size: 24px; font-weight: 600;
    font-variant: small-caps; letter-spacing: .5px;
  }
  .contact__title {
    font-size: 14px; font-weight: 600;
    font-variant: small-caps; letter-spacing: .5px;
    color: var(--text-soft);
    margin-bottom: 22px;
  }
  .contact__line {
    font-family: "Lato", sans-serif;
    font-size: 13px;
    color: var(--text-soft);
    line-height: 1.6;
  }
  .contact__gap { height: 14px; }
  .contact__item {
    display: flex; align-items: center; gap: 8px;
    font-family: "Lato", sans-serif;
    font-size: 13px; color: var(--text-soft);
    line-height: 1.8;
  }
  .contact__item svg { width: 13px; height: 13px; flex: none; }
  .back__band {
    position: absolute;
    left: 0; right: 0; bottom: 0;
    height: 48px;
    background: var(--ink);
    color: var(--white);
    display: flex; align-items: center; justify-content: flex-end;
    padding-right: 40px;
    font-family: "Lato", sans-serif;
    font-size: 14px; letter-spacing: 2px;
  }
</style>
</head>
<body>
  <section class="card card--front">
    <div class="brand">
      <span class="brand__mark"></span>
      <span class="brand__name">Marcie Tolvert Group</span>
    </div>
  </section>

  <section class="card card--back">
    <div class="back__logo">
      <div class="brand">
        <span class="brand__mark"></span>
        <span class="brand__name">Marcie Tolvert Group</span>
      </div>
    </div>
    <div class="back__divider"></div>
    <div class="contact">
      <div class="contact__name">Marcie Tolvert</div>
      <div class="contact__title">Real Estate Luxury Specialist</div>
      <div class="contact__line">DoPLS #04729156</div>
      <div class="contact__gap"></div>
      <div class="contact__line">417 Paseo Vista Linda Suite 310</div>
      <div class="contact__line">Solana Crest, Ca 90417</div>
      <div class="contact__gap"></div>
      <div class="contact__item">
        <svg viewBox="0 0 16 16"><circle cx="8" cy="8" r="8" fill="#0d0d0d"/><path d="M5.2 4.2l1.4-.2.8 1.9-1 .8a6 6 0 0 0 2.9 2.9l.8-1 1.9.8-.2 1.4c-3.7.3-6.9-2.9-6.6-6.6z" fill="#fff"/></svg>
        <span>555.214.7380</span>
      </div>
      <div class="contact__item">
        <svg viewBox="0 0 16 16"><circle cx="8" cy="8" r="8" fill="#0d0d0d"/><path d="M5.2 4.2l1.4-.2.8 1.9-1 .8a6 6 0 0 0 2.9 2.9l.8-1 1.9.8-.2 1.4c-3.7.3-6.9-2.9-6.6-6.6z" fill="#fff"/></svg>
        <span>555.214.7381</span>
      </div>
      <div class="contact__item">
        <svg viewBox="0 0 16 16"><circle cx="8" cy="8" r="8" fill="#0d0d0d"/><rect x="4" y="5.2" width="8" height="5.6" fill="none" stroke="#fff" stroke-width="1"/><path d="M4 5.4l4 3 4-3" fill="none" stroke="#fff" stroke-width="1"/></svg>
        <span>marcie@marcietolvertgroup.com</span>
      </div>
    </div>
    <div class="back__band">www.marcietolvert.com</div>
  </section>
</body>
</html>
```